co working space / serviced office/ business centre

Vandrel - vandrel.in, is a very young brand bieng run by 3 young entrepreneurs. We want to be become out of the league company delivering fabulous and beautiful serviced offices in India and abroad. We hire designers who have made spaces across the world. We want to get visiting card design which gives complete fresh look to the people who carries that card, has to be very impactful and should symbolise happy young and energetic brand. should be completely out of the box thinking of international level, should portray global brand image.

Target Market(s)

Startups, (Small, medium and large corporates)

Industry/Entity Type

Business

Contact Information for Business Card

Name, Email, Address, Mobile number, Landline number, website

Colors

Designer to choose colors to be used in the design.

Requirements
Must have
• Nice new shape
Nice to have
• We want creative cuts, different size and impactful brand clarity
Should not have
• Boring and regular design and shape

```html
<!DOCTYPE html>
<html lang="en">
<head>
<meta charset="utf-8">
<title>Vandrel business card</title>
<link href="https://fonts.googleapis.com/css2?family=Open+Sans:wght@400;600;700&display=swap" rel="stylesheet">
<style>
  :root {
    --bg: #3b3b3d;
    --card: #ffffff;
    --brand-red: #e8383d;
    --ink: #2a2a2a;
    --muted: #4a4a4a;
    --cut: 52px;
  }
  * { box-sizing: border-box; margin: 0; padding: 0; }
  html, body { width: 1200px; height: 864px; overflow: hidden; }
  body {
    background: var(--bg);
    font-family: "Open Sans", Arial, sans-serif;
    position: relative;
  }
  .card-holder {
    position: absolute;
    width: 560px;
    height: 320px;
    filter: drop-shadow(0 10px 18px rgba(0,0,0,.5));
  }
  .holder-front { left: 110px; top: 70px; }
  .holder-back { left: 530px; top: 474px; }
  .card {
    position: relative;
    width: 100%;
    height: 100%;
    background: var(--card);
    clip-path: polygon(0 0, calc(100% - var(--cut)) 0, 100% var(--cut), 100% 100%, var(--cut) 100%, 0 calc(100% - var(--cut)));
  }
  .corner-accent {
    position: absolute;
    width: 90px;
    height: 90px;
    background: var(--brand-red);
  }
  .accent-top { right: 0; top: 0; clip-path: polygon(calc(100% - var(--cut) - 24px) 0, calc(100% - var(--cut)) 0, 100% var(--cut), 100% calc(var(--cut) + 24px)); }
  .accent-bottom { left: 0; bottom: 0; clip-path: polygon(0 calc(100% - var(--cut) - 24px), 0 calc(100% - var(--cut)), var(--cut) 100%, calc(var(--cut) + 24px) 100%); }

  .wordmark {
    display: flex;
    align-items: center;
    gap: 12px;
    color: var(--brand-red);
    font-weight: 700;
    letter-spacing: 2px;
    text-transform: uppercase;
  }
  .wordmark-dot {
    width: 22px; height: 22px;
    border-radius: 50%;
    background: var(--brand-red);
    flex: none;
  }
  .card-front .wordmark {
    position: absolute;
    left: 0; right: 0; top: 118px;
    justify-content: center;
    font-size: 50px;
  }
  .front-url {
    position: absolute;
    left: 0; right: 0; top: 236px;
    text-align: center;
    font-size: 17px;
    color: var(--ink);
  }

  .card-back .wordmark {
    position: absolute;
    left: 34px; top: 134px;
    font-size: 36px;
  }
  .card-back .wordmark-dot { width: 16px; height: 16px; }
  .divider {
    position: absolute;
    left: 300px; top: 56px;
    width: 2px; height: 190px;
    background: var(--brand-red);
  }
  .contact {
    position: absolute;
    left: 326px; top: 52px;
    color: var(--muted);
  }
  .contact-name { color: var(--brand-red); font-weight: 700; font-size: 21px; line-height: 1.1; }
  .contact-role { color: var(--ink); font-weight: 600; font-size: 14px; margin-bottom: 16px; }
  .contact-address { font-size: 14px; line-height: 1.35; margin-bottom: 14px; }
  .contact-list { list-style: none; font-size: 14px; line-height: 1.45; }
  .contact-list li { display: flex; align-items: center; gap: 8px; }
  .contact-list svg { width: 12px; height: 12px; fill: var(--brand-red); flex: none; }
</style>
</head>
<body>
  <div class="card-holder holder-front">
    <section class="card card-front">
      <span class="corner-accent accent-top"></span>
      <span class="corner-accent accent-bottom"></span>
      <div class="wordmark"><span class="wordmark-dot"></span>Vandrel</div>
      <p class="front-url">www.vandrel.in</p>
    </section>
  </div>

  <div class="card-holder holder-back">
    <section class="card card-back">
      <span class="corner-accent accent-top"></span>
      <span class="corner-accent accent-bottom"></span>
      <div class="wordmark"><span class="wordmark-dot"></span>Vandrel</div>
      <div class="divider"></div>
      <div class="contact">
        <p class="contact-name">Mira Kestel</p>
        <p class="contact-role">President</p>
        <p class="contact-address">Street Name Ave, Suite 100<br>State, Zip Code, Country</p>
        <ul class="contact-list">
          <li><svg viewBox="0 0 12 12"><path d="M2.4 0.6l2 2.2-1 1.3c.7 1.6 2 2.9 3.6 3.6l1.3-1 2.2 2-1.1 2.1C5 10.5 1.5 7 0.3 1.7z"/></svg>01 012-345-6789</li>
          <li><svg viewBox="0 0 12 12"><path d="M3 0h6v12H3zM4 1.2v8.3h4V1.2zM5.5 10.3h1v.9h-1z" fill-rule="evenodd"/></svg>01 012-345-6780</li>
          <li><svg viewBox="0 0 12 12"><path d="M0 2h12v8H0zM1 3l5 3.5L11 3z" fill-rule="evenodd"/></svg>info@vandrel.in</li>
          <li><svg viewBox="0 0 12 12"><path d="M6 0a6 6 0 100 12A6 6 0 006 0zm0 1.2c.8.9 1.3 2.5 1.4 4.2H4.6C4.7 3.7 5.2 2.1 6 1.2zM1.3 5.4a4.8 4.8 0 012.2-3.6C3.7 2.2 3.4 3.8 3.4 5.4zm0 1.2h2.1c0 1.6.3 3.2.1 3.6A4.8 4.8 0 011.3 6.6zM6 10.8c-.8-.9-1.3-2.5-1.4-4.2h2.8c-.1 1.7-.6 3.3-1.4 4.2zm2.6-5.4c0-1.6-.3-3.2-.1-3.6a4.8 4.8 0 012.2 3.6zm0 1.2h2.1a4.8 4.8 0 01-2.2 3.6c.2-.4.1-2 .1-3.6z"/></svg>www.vandrel.in</li>
        </ul>
      </div>
    </section>
  </div>
</body>
</html>
```